Tuv9Pen Business Card

I want a two sided business card. I want it similar to my current card, which I provided a picture of, but want my new logo on the front, as well as it saying "veteran owned" somewhere on the front of the card with my face, and new logo. The back of the card can be similar to what I have now, with the qr code that goes to my website "www.tuv9pen.com". I want the color of the card to be a matte color. Feel free to play around with the logo as you see fit. My goal was to mimic the ZEPKA logo since I was in the military.

```html
<!DOCTYPE html>
<html lang="en">
<head>
<meta charset="utf-8">
<title>Tuv9Pen Business Card</title>
<link rel="stylesheet" href="https://fonts.googleapis.com/css2?family=Gelasio:wght@400&family=Montserrat:wght@300;400;600;800&display=swap">
<style>
  :root {
    --backdrop: #e9eaec;
    --sky: #0aa9e2;
    --sky-light: #2dbdf0;
    --sky-pale: #d6f2fb;
    --slate: #3f3f42;
    --slate-light: #535356;
    --ink: #1d1d1f;
    --white: #ffffff;
    --photo-warm: #5b4f45;
    --photo-green: #4b5747;
  }
  * { margin: 0; padding: 0; box-sizing: border-box; }
  html, body { width: 1200px; height: 780px; overflow: hidden; }
  body {
    background: var(--backdrop);
    font-family: "Montserrat", sans-serif;
    position: relative;
  }
  .card {
    position: absolute;
    top: 227px;
    width: 570px;
    height: 326px;
    border-radius: 14px;
    overflow: hidden;
  }
  .card-info { left: 20px; }
  .card-front { left: 610px; background: var(--slate); }
  .card-shapes { position: absolute; inset: 0; }

  /* Info side */
  .person-name {
    position: absolute; left: 52px; top: 62px;
    font-family: "Gelasio", serif; font-weight: 400;
    font-size: 31px; color: var(--ink); letter-spacing: 0.3px;
  }
  .person-title {
    position: absolute; left: 54px; top: 104px;
    font-weight: 300; font-size: 20px; color: var(--ink);
    letter-spacing: 0.6px; text-transform: uppercase;
  }
  .contact-list { position: absolute; left: 56px; top: 150px; list-style: none; }
  .contact-item {
    display: flex; align-items: flex-start; gap: 16px;
    font-size: 14px; color: var(--ink); line-height: 1.3; margin-bottom: 9px;
  }
  .contact-icon { width: 18px; height: 18px; flex: none; margin-top: 2px; }
  .web-line {
    position: absolute; left: 56px; bottom: 14px;
    display: flex; align-items: center; gap: 18px;
    font-weight: 600; font-size: 15px; color: var(--white);
  }
  .brand-name {
    position: absolute; right: 34px; top: 176px;
    font-weight: 800; font-size: 44px; color: var(--white); letter-spacing: 1px;
    white-space: nowrap;
  }

  /* Front side */
  .portrait {
    position: absolute; left: 70px; top: 34px; width: 250px; height: 292px;
    border-radius: 110px 110px 0 0;
    background: linear-gradient(180deg, var(--photo-warm) 0%, var(--photo-green) 100%);
  }
  .front-brand {
    position: absolute; left: 318px; top: 112px;
    font-weight: 800; font-size: 46px; color: var(--white); letter-spacing: 1px;
    white-space: nowrap;
  }
  .veteran-tag {
    position: absolute; right: 26px; bottom: 40px;
    font-weight: 600; font-size: 17px; color: var(--white);
    white-space: nowrap;
  }
</style>
</head>
<body>

  <section class="card card-info" aria-label="Card back with contact details">
    <svg class="card-shapes" viewBox="0 0 570 326" preserveAspectRatio="none" aria-hidden="true">
      <defs>
        <linearGradient id="skyFade" x1="0" y1="1" x2="0.7" y2="0">
          <stop offset="0" stop-color="var(--sky-pale)"/>
          <stop offset="0.55" stop-color="var(--sky-light)"/>
          <stop offset="1" stop-color="var(--sky)"/>
        </linearGradient>
      </defs>
      <rect width="570" height="326" fill="url(#skyFade)"/>
      <polygon points="330,270 478,0 570,0 570,270" fill="var(--sky-light)"/>
      <rect y="270" width="570" height="56" fill="var(--slate)"/>
      <rect x="445" y="270" width="60" height="56" fill="var(--slate-light)"/>
    </svg>

    <h1 class="person-name">Anselmo R Varga III</h1>
    <p class="person-title">Attorney at Law</p>

    <ul class="contact-list">
      <li class="contact-item">
        <svg class="contact-icon" viewBox="0 0 24 24" aria-hidden="true"><circle cx="12" cy="12" r="11" fill="var(--slate)"/><path d="M12 5a4.5 4.5 0 0 0-4.5 4.5C7.5 13 12 18 12 18s4.5-5 4.5-8.5A4.5 4.5 0 0 0 12 5zm0 6.3a1.8 1.8 0 1 1 0-3.6 1.8 1.8 0 0 1 0 3.6z" fill="var(--white)"/></svg>
        <span>2840 Larkspur Ave. Ste 200<br>Dallas, TX 75204</span>
      </li>
      <li class="contact-item">
        <svg class="contact-icon" viewBox="0 0 24 24" aria-hidden="true"><circle cx="12" cy="12" r="11" fill="var(--ink)"/><path d="M8.5 6.5l2 2.3-1.2 1.4c.8 1.7 2 2.9 3.6 3.7l1.4-1.2 2.3 2-1.3 2c-4.4-.6-8-4.2-8.6-8.6z" fill="var(--white)"/></svg>
        <span>877.555.0147</span>
      </li>
      <li class="contact-item">
        <svg class="contact-icon" viewBox="0 0 24 24" aria-hidden="true"><circle cx="12" cy="12" r="11" fill="var(--slate)"/><rect x="7" y="8" width="10" height="8" rx="1" fill="var(--white)"/></svg>
        <span>469.555.0182</span>
      </li>
    </ul>

    <div class="web-line">
      <svg class="contact-icon" viewBox="0 0 24 24" aria-hidden="true"><circle cx="12" cy="12" r="10" fill="none" stroke="var(--white)" stroke-width="1.6"/><ellipse cx="12" cy="12" rx="4.5" ry="10" fill="none" stroke="var(--white)" stroke-width="1.4"/><line x1="2" y1="12" x2="22" y2="12" stroke="var(--white)" stroke-width="1.4"/></svg>
      <span>ano@tuv9pen.com</span>
    </div>

    <p class="brand-name">Tuv9Pen</p>
  </section>

  <section class="card card-front" aria-label="Card front with portrait and brand">
    <svg class="card-shapes" viewBox="0 0 570 326" preserveAspectRatio="none" aria-hidden="true">
      <polygon points="330,326 370,264 570,170 570,326" fill="var(--sky)"/>
    </svg>
    <div class="portrait" role="img" aria-label="Head-and-shoulders portrait of the attorney in a green blazer and white shirt"></div>
    <p class="front-brand">Tuv9Pen</p>
    <p class="veteran-tag">Veteran Owned</p>
  </section>

</body>
</html>
```